App needs a flyer design

We need a flyer design for my new app called'Vexa books', it is a fast, free and fun way to buy and sell used books. I want to see the following features described on the flyer,my first language is not English so I need designers to thinks how to use short language to describe my APP in a short and eye catching way:
selling a book can't be easier on Vexa Books. Scan the barcode or search for the book, then fill in the price,book condition and your contact information.
To buy a book , you can search for listings in your campus and then contact them. You can trade textbooks with other students in campus,.
U can download from Brenzo Loft and Marvle Spin
You need to put my logo(attached file)n the flyer.

Target Market(s)

Uni students

Industry/Entity Type

Trade

Requirements
Must have
• It's features
Nice to have
• The app page as show in the attachment

```html
<!DOCTYPE html>
<html lang="en">
<head>
<meta charset="utf-8">
<title>Vexa Books – flyer</title>
<link rel="stylesheet" href="https://fonts.googleapis.com/css2?family=Josefin+Sans:wght@100;300;400&family=Share+Tech+Mono&display=swap">
<style>
:root{
  --orange:#f2743f;
  --orange-deep:#e8622c;
  --peach:#fde9df;
  --ink:#1a1a1a;
  --grey:#9a9a9a;
  --grey-light:#c4c4c4;
  --rule:#d0d0d0;
  --white:#ffffff;
  --link:#3a3f9e;
  --price:#d0103a;
  --mono:"Share Tech Mono", monospace;
  --sans:"Josefin Sans", sans-serif;
}
*{margin:0;padding:0;box-sizing:border-box}
html,body{width:1200px;height:835px;overflow:hidden;background:var(--white)}
.flyer{position:relative;width:1200px;height:835px;overflow:hidden;font-family:var(--mono);color:var(--ink)}
.abs{position:absolute;white-space:nowrap}

/* left page */
.top-band{left:0;top:0;width:600px;height:66px;background:var(--orange);color:var(--white);font-size:11px;letter-spacing:.6px;text-align:center;line-height:104px}
.top-rule{left:0;top:74px;width:600px;height:6px;background:var(--orange)}
.hero{left:0;top:82px;width:600px;height:238px;background:linear-gradient(90deg,var(--peach) 0%,#fff4ee 60%,var(--white) 100%);border-right:1px solid #f7cdb8}
.brand-title{left:0;top:140px;width:600px;text-align:center;font-family:var(--sans);font-weight:300;font-size:58px;letter-spacing:5px;color:var(--orange)}
.title-bar{left:113px;top:222px;width:377px;height:5px;background:var(--white)}
.tagline{left:60px;top:250px;width:480px;text-align:center;font-family:var(--sans);font-size:19px;letter-spacing:1px;line-height:33px;text-transform:uppercase}
.tagline small{font-size:13px}
.tagline .accent{color:var(--orange)}
.bullets{left:110px;top:346px;list-style:none;color:#555;font-size:12px;letter-spacing:.8px}
.bullets li{position:relative;padding-left:28px;height:33px;line-height:16px}
.bullets li::before{content:"";position:absolute;left:0;top:2px;width:12px;height:12px;border-radius:50%;background:var(--orange)}
.brand-mark{left:130px;top:505px;width:340px;display:flex;align-items:center;justify-content:center;gap:16px}
.brand-mark .square{width:44px;height:44px;background:var(--orange)}
.brand-mark .name{font-family:var(--sans);font-weight:300;font-size:40px;letter-spacing:3px;color:var(--orange)}
.new-app{left:0;top:720px;width:600px;text-align:center;font-size:19px;letter-spacing:1.2px}
.download{left:0;top:773px;width:600px;text-align:center;font-size:12px;letter-spacing:.4px;color:var(--orange)}

/* right page */
.headline{left:676px;top:94px;font-size:34px;line-height:34px;letter-spacing:2px;color:var(--orange)}
.corner-mark{left:1036px;top:88px;width:90px;text-align:center}
.corner-mark .square{width:40px;height:40px;margin:0 auto 10px;background:var(--orange)}
.corner-mark .name{font-size:11px;letter-spacing:1px;color:var(--orange)}
.feature{top:216px;width:170px;color:var(--grey)}
.feature h3{font-weight:400;font-size:12px;letter-spacing:1px;margin-bottom:16px}
.feature li{list-style:none;font-size:6px;letter-spacing:.5px;line-height:11.5px;color:var(--grey-light);text-transform:uppercase}
.feature.buy{left:678px}
.feature.sell{left:857px}

.screen{top:318px;width:147px;height:260px;background:var(--white);box-shadow:0 4px 10px rgba(0,0,0,.18);font-family:Arial,sans-serif;overflow:hidden}
.screen.list{left:678px;background:#ececec}
.screen.scan{left:857px}
.screen .bar{height:28px;background:var(--orange-deep);color:var(--white);position:relative}
.screen .status{font-size:5px;text-align:center;padding-top:2px;opacity:.8}
.search{position:absolute;left:26px;top:14px;width:94px;height:8px;background:var(--white);border-radius:2px;font-size:4px;color:#999;padding-left:4px;line-height:8px}
.item{margin:4px 2px 0;height:42px;background:var(--white);position:relative;padding:4px 5px}
.item .t{font-size:7px;color:var(--link)}
.item .a{font-size:5.5px;color:#888;margin-top:4px}
.item .d{font-size:4.5px;color:#888;position:absolute;left:5px;bottom:4px}
.item .p{position:absolute;right:5px;top:17px;font-size:8.5px;color:var(--price)}
.item:first-of-type{margin-top:2px}
.tabbar{position:absolute;left:0;bottom:0;width:100%;height:26px;background:var(--white);display:flex;justify-content:space-around;align-items:flex-end;padding-bottom:3px;font-size:4.5px;color:#888}
.tabbar span.on{color:var(--orange-deep)}
.scan .bar{font-size:9px;text-align:center}
.scan .bar .back{position:absolute;left:5px;top:12px;font-size:9px}
.scan .bar .ttl{display:block;padding-top:14px}
.scan-frame{position:absolute;left:12px;top:72px;width:122px;height:70px}
.scan-line{position:absolute;left:12px;top:111px;width:122px;height:1px;background:#4a8fd6}
.scan-foot{position:absolute;left:0;bottom:0;width:100%;height:34px;background:#ededed}

.deco{left:970px;top:326px;width:270px;height:364px;background:var(--orange);border-radius:34px;box-shadow:-4px 6px 14px rgba(0,0,0,.25);z-index:1}
.deco .name{position:absolute;left:34px;top:160px;font-family:var(--sans);font-weight:300;font-size:30px;letter-spacing:1px;color:var(--white)}
.slogan{left:600px;top:661px;width:600px;text-align:center;font-size:20px;letter-spacing:.9px;z-index:2}
.slogan-rule{left:600px;top:689px;width:600px;height:5px;background:var(--rule);z-index:2}
.trade{left:600px;top:705px;width:600px;text-align:center;font-size:15px;letter-spacing:1.4px;color:var(--grey-light)}
.more{left:600px;top:741px;width:600px;text-align:center;font-size:12px;letter-spacing:1.2px;color:var(--grey)}
.bottom-band{left:600px;top:768px;width:600px;height:44px;background:var(--orange);color:var(--white);font-size:6px;letter-spacing:1px;text-align:center;line-height:44px}
.bottom-rule{left:600px;top:826px;width:600px;height:9px;background:var(--orange)}
</style>
</head>
<body>
<main class="flyer">
  <!-- left page -->
  <div class="abs top-band">SELL YOUR BOOKS FAST AND FREE WITH THE VEXA BOOKS APP FROM HOME OR CAMPUS</div>
  <div class="abs top-rule"></div>
  <div class="abs hero"></div>
  <h1 class="abs brand-title">Vexa Books</h1>
  <div class="abs title-bar"></div>
  <p class="abs tagline"><small>A</small> Fast, Free <small>and</small> Fun <small>way to</small> Buy and Sell<br>Your used <span class="accent">Books</span></p>
  <ul class="abs bullets">
    <li>GET ACCESS TO A WHOLE NEW BOOKSTORE</li>
    <li>AND MAKE MONEY WITH YOUR USED BOOKS AT THE SAME TIME</li>
  </ul>
  <div class="abs brand-mark"><span class="square"></span><span class="name">Vexa Books</span></div>
  <p class="abs new-app">THE NEW APP</p>
  <p class="abs download">DOWNLOAD FROM BRENZO LOFT OR MARVLE SPIN</p>

  <!-- right page -->
  <h2 class="abs headline">SELLING A BOOK<br>WAS NEVER EASIER</h2>
  <div class="abs corner-mark"><div class="square"></div><div class="name">VEXA BOOKS</div></div>

  <section class="abs feature buy">
    <h3>BUY USED BOOKS</h3>
    <ul><li>Search for listings on your own campus</li><li>Contact them</li><li>Trade textbooks with other students</li></ul>
  </section>
  <section class="abs feature sell">
    <h3>SELL USED BOOKS</h3>
    <ul><li>Scan the barcode / search for the book</li><li>Fill in the price you want to sell it for</li><li>Fill in the book condition</li><li>Fill in your contact information</li></ul>
  </section>

  <div class="abs screen list">
    <div class="bar"><div class="status">9:41 PM</div><div class="search">title, code, author</div></div>
    <div class="item"><div class="t">Tales of the Quiet Harbor</div><div class="a">Merrow, Ilsa Dane.</div><div class="d">At February 11, 2015</div><div class="p">$ 58.00</div></div>
    <div class="item"><div class="t">Tales of the Quiet Harbor</div><div class="a">Merrow, Ilsa Dane.</div><div class="d">At February 7, 2015</div><div class="p">$ 32.00</div></div>
    <div class="item"><div class="t">Tales of the Quiet Harbor</div><div class="a">Merrow, Ilsa Dane.</div><div class="d">At February 6, 2015</div><div class="p">$ 76.00</div></div>
    <div class="item"><div class="t">Tales of the Quiet Harbor</div><div class="a">Merrow, Ilsa Dane.</div><div class="d">At February 1, 2015</div><div class="p">$ 14.00</div></div>
    <div class="tabbar"><span class="on">Home</span><span>Sell</span><span>Scan</span><span>My Ads</span></div>
  </div>

  <div class="abs screen scan">
    <div class="bar"><span class="back">&lsaquo;</span><span class="ttl">Scan</span></div>
    <svg class="scan-frame" viewBox="0 0 122 70" aria-hidden="true">
      <path d="M1 9V1h9M112 1h9v8M121 61v8h-9M10 69H1v-8" fill="none" stroke="#3b6fb0" stroke-width="1.5"/>
    </svg>
    <div class="scan-line"></div>
    <div class="scan-foot"></div>
  </div>

  <div class="abs deco"><span class="name">Vexa Books</span></div>

  <p class="abs slogan">YOUR LOCAL BOOKSTORE JUST GOT A LITTLE BIGGER</p>
  <div class="abs slogan-rule"></div>
  <p class="abs trade">TRADE YOUR TEXTBOOKS WITH STUDENTS FROM YOUR CAMPUS</p>
  <p class="abs more">AND MUCH MORE...</p>
  <div class="abs bottom-band">THE VEXA BOOKS APP IS AVAILABLE ON BRENZO LOFT OR MARVLE SPIN</div>
  <div class="abs bottom-rule"></div>
</main>
</body>
</html>
```